Psychiatrist/ Psychotherapist needs a letterhead design

I am a Psychiatrist working in private practice. I work as a psychotherapist and treat patients with depression, anxiety, post traumatic stress and relationship problems. I need a letterhead which is elegant and professional. I would like to see designs using colours such as blues and greys.
I would like the information on the letterhead split between the top and bottom of the page to give it a look of balance.
I want it to look elegant, feminine and upmarket. I don't want it to look too corporate but to show some flair and to be a bit artistic.

Other doctors, specialists and agencies who have referred patients to me.

Work

Script

Requirements
Must have
• My name and my profession psychiatrist need to be highlighted and prominent. It needs to be professional looking and elegant without being old fashioned or too conservative.
Nice to have
• Balance between the top and bottom of the page.
Should not have
• I don't want fonts which are old and too traditional.

```html
<!DOCTYPE html>
<html lang="en">
<head>
<meta charset="utf-8">
<title>Letterhead – Dr. Helena Marlowe</title>
<link rel="stylesheet" href="https://fonts.googleapis.com/css2?family=Pinyon+Script&family=Tinos&family=Arimo&display=swap">
<style>
  :root {
    --canvas-bg: #e9e8e5;
    --paper: #ffffff;
    --band: #e7f0f4;
    --leaf-light: #eaf3f7;
    --leaf-mid: #cfe3ec;
    --ink: #1b1b1b;
    --ink-soft: #333333;
    --accent: #7fb3c9;
  }
  * { margin: 0; padding: 0; box-sizing: border-box; }
  html, body { width: 1200px; height: 1000px; overflow: hidden; }
  body { background: var(--canvas-bg); position: relative; }

  .letterhead {
    position: absolute;
    left: 280px; top: 47px;
    width: 640px; height: 905px;
    background: var(--paper);
    box-shadow: 0 4px 18px rgba(0,0,0,0.12);
    overflow: hidden;
  }

  .foliage {
    position: absolute;
    border-radius: 50%;
  }
  .foliage--top {
    right: -60px; top: -40px;
    width: 220px; height: 170px;
    background: radial-gradient(ellipse at 70% 30%, var(--leaf-mid) 0%, var(--leaf-light) 45%, rgba(255,255,255,0) 72%);
  }
  .foliage--bottom {
    right: -70px; bottom: 40px;
    width: 360px; height: 300px;
    background: radial-gradient(ellipse at 60% 60%, var(--leaf-mid) 0%, var(--leaf-light) 45%, rgba(255,255,255,0) 72%);
  }

  .header-band {
    position: absolute;
    left: 22px; right: 0; top: 28px;
    height: 87px;
    background: var(--band);
    display: flex;
    align-items: center;
    justify-content: space-between;
    padding: 0 40px 0 26px;
  }
  .header-band__name {
    font-family: "Pinyon Script", cursive;
    font-size: 40px;
    color: var(--ink);
    font-weight: 400;
  }
  .header-band__credentials {
    text-align: right;
    font-family: "Tinos", serif;
    font-size: 14px;
    line-height: 20px;
  }
  .header-band__degree { color: var(--ink); }
  .header-band__profession { color: var(--accent); }

  .letter-body {
    position: absolute;
    left: 41px; top: 260px;
    width: 560px;
    font-family: "Arimo", sans-serif;
    font-size: 9.6px;
    line-height: 12.8px;
    color: var(--ink-soft);
  }
  .letter-body p { margin-bottom: 23px; }
  .letter-body .salutation { margin-bottom: 27px; }
  .letter-body .tight { margin-bottom: 12px; }

  .footer-band {
    position: absolute;
    left: 33px; right: 33px; top: 820px;
    height: 62px;
    background: var(--band);
    font-family: "Tinos", serif;
    font-size: 11.5px;
    line-height: 18px;
    color: var(--ink);
    text-align: center;
    padding-top: 12px;
    word-spacing: 1px;
  }
  .footer-band span + span { margin-left: 12px; }
</style>
</head>
<body>
  <article class="letterhead">
    <div class="foliage foliage--top" role="img" aria-label="Soft pale blue leaf pattern in the top corner"></div>
    <div class="foliage foliage--bottom" role="img" aria-label="Soft pale blue leaf pattern in the lower corner"></div>

    <header class="header-band">
      <h1 class="header-band__name">Dr. Helena Marlowe</h1>
      <div class="header-band__credentials">
        <div class="header-band__degree">Dr. Helena Marlowe, B. Med</div>
        <div class="header-band__profession">FRANZCP Psychiatrist</div>
      </div>
    </header>

    <section class="letter-body">
      <p class="salutation">Lorem ipsum dolor sit amet,</p>
      <p>everti epicuri eu sed, graeco bonorum eu nam, vix duis partem prodesset ad.<br>
      Usu ne veri dolor virtute. Ei nec oratio delenit, mei libris option ei. Mel ad assum utroque perpetua, vide habeo mei ut.</p>
      <p>Pro eu molestiae percipitur, convenire forensibus ei usu. Ei inani interesset vis, fabellas nominati eos ei,<br>
      modus erroribus dissentias eu nam.<br>
      Eu nec facilis necessitatibus, te dico dictas virtute eum, quo ne consul copiosae. In qui viderer ponderum.</p>
      <p>Ut mel recusabo mediocritatem. Ne has quas alienum. Id vel utamur consulatu quaerendum, has sale natum utroque ne.<br>
      Admodum deserunt an mea, at nec dicit rationibus, ad indoctum consulatu has. Usu ut vivendo deseruisse contentiones.<br>
      Et usu reque reprehendunt.</p>
      <p>Sea ut inani epicuri, in has modus vitae doctus. Cu eos nemore eruditi ponderum.<br>
      Tritani detraxit contentiones mea in. Ut pri decore nostrud partiendo, ei vel clita noster appetere.</p>
      <p class="tight">His vidisse urbanitas ne, in quo rebum utroque accumsan.<br>
      Nam maluisset scriptorem ne, quo ex paulo appareat erroribus, sit rebum qualisque ex.</p>
      <p>Modo omittantur ex ius. Veniam pericula an ius, ut sea duis appetere singulis. Euismod delicata conc<br>
      ludaturque eu eos,<br>
      ne lorem oratio delectus sea. Eum et corpora apeirian repudiare, ea sea expetenda consetetur delicatissimi.</p>
      <p>ea sea expetenda consetetur delicatissimi.</p>
    </section>

    <footer class="footer-band">
      <div><span>14 Garden Lane, Norwood, SA 5067</span><span>hmarlowe@mailpost.net</span></div>
      <div><span>Tel: (08) 8100 4721</span><span>Fax: (08) 8100 4722</span><span>Mob: 0412555019</span></div>
    </footer>
  </article>
</body>
</html>
```